Website design for management consulting firm

We need a web design for a new consulting company based in Boston, MA called "Quillmoor Ridge Consulting." This webpage will be simple home page, with a "contact us" page, that describes the services of the consulting firm. The company provides strategic planning, business assessment, process re-designs, and other management consulting functions. I would like the website to look high-tech. A logo was already created via Artsy Hive.

Target Market(s)

Other business owners across a wide spectrum of industries - from IT to retail.

Industry/Entity Type

It Company

Number of Pages Required

3 page

Colors
0455a3
ffffff

Requirements
Must have
• Front page that provides generic text / overview of the firm. A "services" tab that describes consulting services. A "contact us" tab that provides either a form to contact us or just the contact email address of the company. info@quillmoorridgeconsulting.example

```html
<!DOCTYPE html>
<html lang="en">
<head>
<meta charset="utf-8">
<title>Contact Us – Quillmoor Ridge Consulting</title>
<link rel="stylesheet" href="https://fonts.googleapis.com/css2?family=Tinos&display=swap">
<style>
  :root {
    --brand-blue: #04608a;
    --sea-teal: #18a99c;
    --nav-teal: #1fb1a3;
    --ink-dark: #1f1d1e;
    --text-blue: #0b5a82;
    --paper: #ffffff;
    --field-border: #dcdcdc;
  }
  * { box-sizing: border-box; margin: 0; padding: 0; }
  html, body {
    width: 1108px;
    height: 1200px;
    overflow: hidden;
  }
  body {
    background: var(--sea-teal);
    font-family: "Tinos", "Times New Roman", serif;
    position: relative;
  }
  .site-header {
    position: absolute;
    left: 0; top: 0;
    width: 1108px; height: 243px;
    background: var(--paper);
  }
  .brand-square {
    position: absolute;
    left: 0; top: 0;
    width: 227px; height: 243px;
    background: var(--brand-blue);
  }
  .brand-name {
    position: absolute;
    left: 290px; top: 38px;
    color: var(--ink-dark);
    font-size: 78px;
    font-weight: 400;
    line-height: 88px;
  }
  .main-nav {
    position: absolute;
    left: 0; top: 243px;
    width: 1108px; height: 87px;
    background: var(--brand-blue);
  }
  .main-nav a {
    position: absolute;
    top: 6px;
    color: var(--nav-teal);
    font-size: 69px;
    line-height: 74px;
    text-decoration: none;
    white-space: nowrap;
  }
  .nav-home { left: 68px; }
  .nav-services { left: 420px; }
  .nav-contact { left: 772px; }
  .contact-intro {
    position: absolute;
    left: 10px; top: 350px;
    color: var(--text-blue);
    font-size: 25px;
    line-height: 35px;
  }
  .contact-form {
    position: absolute;
    left: 10px; top: 435px;
  }
  .message-field {
    display: block;
    width: 751px; height: 247px;
    background: var(--paper);
    border: 4px solid var(--field-border);
    resize: none;
    font-family: inherit;
    font-size: 24px;
  }
  .submit-button {
    display: block;
    margin-top: 6px;
    width: 186px; height: 60px;
    background: var(--paper);
    border: none;
    color: var(--text-blue);
    font-family: inherit;
    font-size: 42px;
    text-align: left;
    padding-left: 20px;
  }
</style>
</head>
<body>
  <header class="site-header">
    <div class="brand-square" role="img" aria-label="Quillmoor Ridge Consulting brand square in brand blue"></div>
    <div class="brand-name">Quillmoor Ridge<br>Consulting</div>
  </header>
  <nav class="main-nav">
    <a class="nav-home" href="#">Home</a>
    <a class="nav-services" href="#">Services</a>
    <a class="nav-contact" href="#">Contact Us</a>
  </nav>
  <main>
    <div class="contact-intro">
      <p>Contact us by email at: info@quillmoorridgeconsulting.example</p>
      <p>Or fill out this form:</p>
    </div>
    <form class="contact-form">
      <textarea class="message-field" aria-label="Message"></textarea>
      <button class="submit-button" type="button">Submit</button>
    </form>
  </main>
</body>
</html>
```